Kindle Grove Wording For Logo & Business card

I have the logo, I just need the "kindle Grove" wording to go with it, and a business card design. The only thing on the business card is the website info. We provide nature connection experiences, and bolster these efforts through writing and host a platform for community around it.

I also have an idea of what it could look like (sketch), though I'm really not sure how it would come out. I am open to the best design and happy to consider original artwork. You can see what the site is about at KindleGrove.com.

Contact Information for Business Card

The only thing on the business card is the website info and the design. I will put other messaging on the back.

Website lettering (KindleGrove.com) in Montserrat

Logo Text

Kindle Grove (letters optional)

Font styles to use
Other font styles liked:
• montserrat

```html
<!DOCTYPE html>
<html lang="en">
<head>
<meta charset="utf-8">
<title>Kindle Grove — Business Card</title>
<link rel="stylesheet" href="https://fonts.googleapis.com/css2?family=Montserrat:wght@400;500&display=swap">
<style>
  :root {
    --page: #2b2f35;
    --card: #eeeeef;
    --photo-light: #f3f3f2;
    --photo-mid: #d9dcd6;
    --photo-deep: #c3c8c0;
    --purple: #5a2d78;
    --purple-text: #5b3a73;
    --mark: #2a1d45;
    --ink: #3a3a3a;
    --orange: #e6742a;
  }
  * { box-sizing: border-box; margin: 0; padding: 0; }
  html, body { width: 1200px; height: 780px; overflow: hidden; }
  body {
    background: var(--page);
    font-family: "Montserrat", sans-serif;
    display: flex; align-items: center; justify-content: center;
  }
  .card {
    position: relative;
    width: 1050px; height: 600px;
    border-radius: 30px;
    background: var(--card);
    overflow: hidden;
    border-bottom: 8px solid var(--purple);
  }
  .card__photo {
    position: absolute; inset: 0;
    background:
      radial-gradient(ellipse 420px 260px at 70% 80%, var(--photo-light), transparent 70%),
      radial-gradient(ellipse 380px 300px at 85% 20%, var(--photo-deep), transparent 75%),
      radial-gradient(ellipse 300px 260px at 10% 85%, var(--photo-mid), transparent 75%),
      linear-gradient(160deg, var(--photo-light), var(--photo-mid) 55%, var(--photo-light));
    opacity: .85;
  }
  .card__brand {
    position: absolute; left: 0; top: 0; bottom: 0; width: 300px;
    display: flex; flex-direction: column; align-items: center; justify-content: center;
    gap: 34px;
    background: rgba(255,255,255,.35);
  }
  .brand__disc {
    width: 190px; height: 190px; border-radius: 50%;
    background: var(--mark);
    box-shadow: 0 0 0 8px rgba(255,255,255,.7);
  }
  .brand__name {
    font-size: 26px; font-weight: 400; letter-spacing: 1px;
    color: var(--ink); text-transform: uppercase;
  }
  .card__divider {
    position: absolute; top: 0; bottom: 0; left: 300px; width: 26px;
    border-left: 12px solid var(--purple);
    border-right: 5px solid var(--purple);
  }
  .card__details {
    position: absolute; left: 400px; right: 40px; top: 0; bottom: 0;
    display: flex; align-items: center;
  }
  .website {
    display: flex; align-items: center; gap: 22px;
    font-size: 36px; font-weight: 400; color: var(--purple-text);
  }
  .website svg { width: 44px; height: 44px; flex: none; }
</style>
</head>
<body>
  <main class="card">
    <div class="card__photo" role="img" aria-label="Faded aerial photograph of a raft on white-water river rapids between rocky banks"></div>

    <section class="card__brand">
      <div class="brand__disc"></div>
      <p class="brand__name">Kindle Grove</p>
    </section>

    <div class="card__divider"></div>

    <section class="card__details">
      <p class="website">
        <svg viewBox="0 0 40 40" aria-hidden="true">
          <circle cx="20" cy="20" r="18" fill="var(--orange)"/>
          <g fill="none" stroke="#fff" stroke-width="2">
            <ellipse cx="20" cy="20" rx="7" ry="17"/>
            <line x1="3" y1="20" x2="37" y2="20"/>
            <line x1="20" y1="3" x2="20" y2="37"/>
            <path d="M6 11h28M6 29h28"/>
          </g>
        </svg>
        www.kindlegrove.com
      </p>
    </section>
  </main>
</body>
</html>
```